Pinecrest 71 Studios needs a web design

We need a website design for a California based visual effects (VFX) company to show potential clients and employees who we are and what we do. We are currently focusing on compositing based tasks such as but not limited to multi-pass composites, green screen extraction, rotoscope, paint fixes and retimes. We like imagery that makes people think of 'California' such as the state flag, sunshine and the beach. The website should send a message that although we are a new company, we are not new to the vfx industry. The website needs to be compatible with mobile devices. We also need the ability to edit and modify the site.

Target Market(s)

Studio executive, producers and potential employees.

Industry/Entity Type

Flag

Coding

Coded - Design and coding required

Number of Pages Required

4 page

Font styles to use
Serif
Sans Serif

Requirements
Must have
• Must have space for company and individual biographies. Must have a page for a credits list and show reel. Must also have space for contact info ex. maps, email, social media.

```html
<!DOCTYPE html>
<html lang="en">
<head>
<meta charset="utf-8">
<title>Pinecrest 71 Studios</title>
<link rel="stylesheet" href="https://fonts.googleapis.com/css2?family=Lato:wght@300;400;700&family=Open+Sans:wght@400;700&display=swap">
<style>
:root{
  --green-top:#2c5637;
  --green-mid:#3b6a44;
  --night:#0c1819;
  --night-deep:#081213;
  --teal-line:#1f5a50;
  --orange:#d98b3c;
  --tan:#c49a6c;
  --tan-field:#c8956a;
  --red:#b3262a;
  --red-text:#e98a6d;
  --white:#ffffff;
  --body:#b8c2c0;
  --about-text:#dfe6e4;
  --link-green:#4fae74;
  --footer-top:#6a5030;
  --footer-bottom:#3b2e20;
}
*{margin:0;padding:0;box-sizing:border-box}
html,body{width:732px;height:1200px;overflow:hidden}
body{position:relative;background:var(--night);font-family:"Lato",sans-serif;color:var(--white)}
.abs{position:absolute}
.page-bg{left:0;top:0;width:732px;height:1200px;
  background:linear-gradient(180deg,var(--green-top) 0,var(--green-mid) 260px,#2e4f36 350px,#13211f 400px,var(--night) 440px,var(--night-deep) 1060px)}
.hero-grass{left:150px;top:150px;width:440px;height:260px;
  background:radial-gradient(ellipse at 50% 70%,rgba(214,210,60,.45),rgba(170,190,40,.2) 45%,rgba(0,0,0,0) 70%)}
.brand-dot{left:326px;top:5px;width:8px;height:8px;border-radius:50%;background:var(--red)}
.brand-name{left:266px;top:43px;width:200px;text-align:center;font-weight:700;font-size:8.5px;letter-spacing:.2px}
.main-nav{left:0;top:60px;width:732px;height:20px}
.main-nav a{position:absolute;top:0;font-size:7.5px;color:var(--tan);text-decoration:none;text-transform:uppercase}
.main-nav a.active{color:var(--white)}
.nav-shadow{left:222px;top:72px;width:290px;height:6px;background:radial-gradient(ellipse at 50% 0,rgba(0,0,0,.35),rgba(0,0,0,0) 70%)}
.social-squares{display:flex;gap:3px}
.social-squares span{width:9px;height:9px;background:var(--tan);border-radius:1px;display:block}
.hero-title{left:0;top:109px;width:732px;text-align:center;font-weight:300;font-size:27px}
.hero-sub{left:0;top:143px;width:732px;text-align:center;font-family:"Open Sans",sans-serif;font-weight:700;font-size:8.8px;color:var(--orange);letter-spacing:0}
.btn{background:var(--red);color:var(--red-text);font-size:8px;text-transform:uppercase;display:flex;align-items:center;justify-content:center;border-radius:1px;box-shadow:0 2px 3px rgba(0,0,0,.35)}
.hero-btn{left:308px;top:178px;width:116px;height:23px;font-size:9px}
.tile{width:116px;height:65px}
.tile.featured{outline:2px solid var(--red);outline-offset:-2px}
.tile-caption{left:6px;top:38px;font-size:9px;text-transform:uppercase;line-height:1}
.tile-caption small{display:block;font-size:5.5px;text-transform:none;color:#ccc;margin-top:2px}
.section-label{font-family:"Open Sans",sans-serif;font-weight:700;font-size:6.5px;color:var(--orange);text-transform:uppercase;letter-spacing:.3px}
.rule{height:1px;background:var(--teal-line)}
.news{width:116px}
.news h3{font-family:"Lato",sans-serif;font-size:6.5px;font-weight:400;line-height:1.3;text-transform:uppercase;height:17px}
.news time{display:block;text-align:right;font-size:3.5px;color:var(--link-green);margin-top:1px}
.news .bar{height:2px;background:var(--red);margin:4px 0 6px}
.news p{font-size:4.3px;line-height:1.6;color:var(--body)}
.about-text{left:308px;top:518px;width:240px;font-size:4.8px;line-height:1.65;color:var(--about-text)}
.read-btn{left:480px;top:554px;width:67px;height:19px;font-size:6px}
.people-panel{left:183px;top:608px;width:366px;height:122px;background:radial-gradient(ellipse at 45% 15%,#1f4b4c,#133033 60%,#102527)}
.portrait{width:80px;height:80px;border-radius:50%;border:2px solid #d7d9d6;background:radial-gradient(circle at 50% 40%,#8a8f92,#3b4a55)}
.bio h4{font-family:"Lato",sans-serif;font-size:6.5px;font-weight:400;text-transform:uppercase;margin-bottom:7px}
.bio p{font-size:4.5px;line-height:1.6;color:var(--body);width:86px}
.bio .more{display:block;text-align:right;font-size:3.6px;color:var(--link-green);margin-top:5px;text-transform:uppercase}
.map{left:186px;top:768px;width:171px;height:110px;background:linear-gradient(135deg,#e6e2d8,#d7d2c4 50%,#cfcab9)}
.map-card{left:186px;top:842px;width:164px;height:28px;background:rgba(74,58,40,.85);padding:5px 8px;font-size:4.8px;line-height:1.45;color:var(--tan)}
.form-label{left:187px;font-size:5px}
.field{left:235px;width:116px;background:var(--tan-field)}
.submit-btn{left:284px;top:1010px;width:67px;height:18px;font-size:6px}
.feed{left:375px;top:768px;width:171px;height:259px;background:#1c2326;border:1px solid #3d4649;font-family:"Open Sans",sans-serif}
.feed-head{height:10px;background:#2a3336;font-size:4px;padding:3px 3px;color:#dfe3e3}
.feed-post{position:absolute;left:4px;width:157px;background:#d8dde0;border:1px solid #6b7579;padding:4px;color:#333;font-size:3.8px;line-height:1.4}
.feed-post b{color:#1c2326}
.feed-photo{height:54px;margin:4px 0;background:linear-gradient(180deg,#2c3d6e,#34456f 60%,#c9b9a4)}
.feed-avatar{width:10px;height:10px;background:#4b5558;float:left;margin-right:3px}
.footer{left:0;top:1063px;width:732px;height:137px;background:linear-gradient(180deg,var(--footer-top),#574128 45%,var(--footer-bottom))}
.footer-scene{left:190px;top:1100px;width:350px;height:100px;background:radial-gradient(ellipse at 50% 30%,rgba(210,175,120,.35),rgba(0,0,0,0) 70%)}
.footer-nav a{position:absolute;top:0;font-size:7.5px;color:var(--white);text-decoration:none;text-transform:uppercase}
.copyright{left:0;top:1093px;width:732px;text-align:center;font-size:5.5px}
.footer-brand{left:0;top:1155px;width:732px;display:flex;justify-content:center;align-items:center;gap:5px;font-weight:700;font-size:10px}
.footer-brand span.dot{width:8px;height:8px;border-radius:50%;background:var(--red)}
</style>
</head>
<body>
<div class="abs page-bg"></div>
<div class="abs hero-grass" role="img" aria-label="Tall yellow-green grass blades rising behind the gallery"></div>

<header>
  <span class="abs brand-dot"></span>
  <div class="abs brand-name">PINECREST 71 STUDIOS</div>
  <nav class="abs main-nav">
    <a class="active" href="#" style="left:272px">Work</a>
    <a href="#" style="left:309px">Company</a>
    <a href="#" style="left:357px">People</a>
    <a href="#" style="left:397px">Reel</a>
    <a href="#" style="left:428px">Contact</a>
    <div class="abs social-squares" style="left:510px;top:0"><span></span><span></span><span></span></div>
  </nav>
  <div class="abs nav-shadow"></div>
</header>

<section class="hero">
  <h1 class="abs hero-title">Large Experience in Visuals</h1>
  <p class="abs hero-sub">FOR THE TOP ADVERTISING, TELEVISION, MOTION PICTURE AND GAMING</p>
  <a class="abs btn hero-btn">See our work</a>
</section>

<section class="gallery">
  <div class="abs tile featured" style="left:186px;top:242px;background:linear-gradient(135deg,#6d5a5a,#3a3438 60%,#2a2a30)" role="img" aria-label="Film still: a lone figure in a snowy landscape">
    <div class="abs tile-caption">Starward<small>Some Pictures / USA</small></div>
  </div>
  <div class="abs tile" style="left:308px;top:242px;background:linear-gradient(160deg,#d2a35a,#8a4d2a 50%,#3b2a22)" role="img" aria-label="Film still: a warrior before a fiery battlefield"></div>
  <div class="abs tile" style="left:430px;top:242px;background:linear-gradient(135deg,#f0b870,#c0403a 45%,#4a4f8a)" role="img" aria-label="Film still: a hero streaking with light"></div>
  <div class="abs tile" style="left:186px;top:313px;background:linear-gradient(180deg,#6fc5e0,#2a8fbf 55%,#154f7a)" role="img" aria-label="Film still: a dolphin leaping underwater"></div>
  <div class="abs tile" style="left:308px;top:313px;background:linear-gradient(180deg,#8f9296,#4a4d52 60%,#25282c)" role="img" aria-label="Film still: a close-up of a primate's eyes"></div>
  <div class="abs tile" style="left:430px;top:313px;background:linear-gradient(160deg,#5d8a3a,#2f5a2a 55%,#c9a23a)" role="img" aria-label="Film still: a round yellow door in a grassy hillside"></div>
</section>

<section class="headlines">
  <h2 class="abs section-label" style="left:186px;top:403px">Headlines</h2>
  <div class="abs rule" style="left:186px;top:413px;width:360px"></div>
  <article class="abs news" style="left:186px;top:422px">
    <h3>Lorem ipsum dolor sit amet, consectetur</h3>
    <time>JANUARY 08, 2015</time><div class="bar"></div>
    <p>Nam et rutrum lectus, a dictum mi. Vestibulum turpis sapien, tempus eu tempor a, suscipit quis lectus. Ut neque felis, hendrerit quis luctus sit amet, hendrerit at ipsum.</p>
  </article>
  <article class="abs news" style="left:310px;top:422px">
    <h3>Duis aliquet nibh nec nisi<br>luctus, eget fermentum est</h3>
    <time>JANUARY 08, 2015</time><div class="bar"></div>
    <p>Nam et rutrum lectus, a dictum mi. Vestibulum turpis sapien, tempus eu tempor a, suscipit quis lectus. Ut neque felis, hendrerit quis luctus sit amet, hendrerit at ipsum.</p>
  </article>
  <article class="abs news" style="left:430px;top:422px">
    <h3>Lorem ipsum dolor sit amet, consectetur</h3>
    <time>JANUARY 08, 2015</time><div class="bar"></div>
    <p>Nam et rutrum lectus, a dictum mi. Vestibulum turpis sapien, tempus eu tempor a, suscipit quis lectus. Ut neque felis, hendrerit quis luctus sit amet, hendrerit at ipsum.</p>
  </article>
  <div class="abs rule" style="left:186px;top:484px;width:482px"></div>
</section>

<section class="about">
  <div class="abs" style="left:186px;top:500px;width:116px;height:78px;background:linear-gradient(160deg,#9bb6e6,#5e7fbf 45%,#2a3c5e 80%,#1c2a2c)" role="img" aria-label="Modern glass office building against a blue sky"></div>
  <h2 class="abs section-label" style="left:309px;top:502px">About us</h2>
  <div class="abs rule" style="left:308px;top:511px;width:360px"></div>
  <p class="abs about-text">Formed in 2014, Pinecrest 71 Studios is a visual effects studio based in Seaview, CA. Taking their name from early Californian history, Pinecrest 71 Studios looks to continue the Golden State's tradition of strong and reliable visual effects. With close to 20 years in the vfx community, Pinecrest 71 Studios has the ability to service feature films, television, and commercials.</p>
  <a class="abs btn read-btn">Keep reading</a>
</section>

<section class="abs people-panel">
  <div class="abs portrait" style="left:5px;top:20px" role="img" aria-label="Portrait photo of Owen"></div>
  <div class="abs bio" style="left:92px;top:24px">
    <h4>About Owen:</h4>
    <p>Owen Mitchell Marlowe grew up in Los Angeles and by the young age of 17 was working in the film industry as an on-set Production Assistant on 'The Courier'. By 1999, he began his long journey in to visual effects as a visual effects coordinator at Brightwater Pictures.</p>
    <span class="more">» Keep reading</span>
  </div>
  <div class="abs portrait" style="left:190px;top:20px" role="img" aria-label="Portrait photo of Danny"></div>
  <div class="abs bio" style="left:277px;top:24px">
    <h4>About Danny:</h4>
    <p>Danny Larkin grew up in San Jose, CA reading comic books and Nightcrawl. Art and movies have always been a part of daily life. In 1997 Danny was given a chance to begin working in the visual effects industry as a generalist.</p>
    <span class="more" style="margin-top:14px">» Keep reading</span>
  </div>
</section>

<section class="contact">
  <h2 class="abs section-label" style="left:187px;top:751px">Contact us</h2>
  <div class="abs rule" style="left:186px;top:761px;width:171px"></div>
  <div class="abs map" role="img" aria-label="Street map around the studio location"></div>
  <div class="abs map-card">418 Cypress Row<br>Seaview, CA 90000<br>P: +1 310 555 0142</div>
  <label class="abs form-label" style="top:899px">Name</label>
  <div class="abs field" style="top:894px;height:15px"></div>
  <label class="abs form-label" style="top:921px">Email</label>
  <div class="abs field" style="top:917px;height:15px"></div>
  <label class="abs form-label" style="top:945px">Message (optional)</label>
  <div class="abs field" style="top:940px;height:61px"></div>
  <a class="abs btn submit-btn">Submit</a>
</section>

<section class="social">
  <h2 class="abs section-label" style="left:375px;top:751px">Social media</h2>
  <div class="abs rule" style="left:375px;top:761px;width:171px"></div>
  <div class="abs feed">
    <div class="feed-head">Find us online</div>
    <div class="abs" style="left:4px;top:14px;font-size:4.5px;color:#dfe3e3"><span class="feed-avatar"></span><b style="color:#fff">Harbor Lane FX</b><br>Liked page</div>
    <div class="feed-post" style="top:30px;height:172px">
      <span class="feed-avatar"></span><b>Harbor Lane FX</b><br>Posted recently<br style="clear:both">
      <p style="margin-top:4px">Award season is nearly upon us and the team is proud to see several projects we worked on earn nominations this month.</p>
      <div class="feed-photo" role="img" aria-label="Group photo of award nominees on stage"></div>
      <p style="font-size:5px;color:#1c2326"><b>Nominations 2015 - Silver Reel Awards Official Site</b></p>
      <p>The full list of nominees across film and television is now online, including best picture and best visual effects.</p>
    </div>
    <div class="feed-post" style="top:206px;height:44px">
      <span class="feed-avatar"></span><b>Harbor Lane FX</b><br>Posted last week<br style="clear:both">
      <p style="margin-top:3px">Our team put together the opening title animations for a new drama series. Watch the reel on our page.</p>
    </div>
  </div>
</section>

<footer>
  <div class="abs footer"></div>
  <div class="abs footer-scene" role="img" aria-label="Faint sunset beach with a wooden pier"></div>
  <nav class="abs footer-nav" style="left:0;top:1078px;width:732px;height:12px">
    <a href="#" style="left:272px">Work</a>
    <a href="#" style="left:309px">Company</a>
    <a href="#" style="left:357px">People</a>
    <a href="#" style="left:397px">Reel</a>
    <a href="#" style="left:428px">Contact</a>
  </nav>
  <p class="abs copyright">Pinecrest 71 Studios All rights reserved 2015</p>
  <div class="abs social-squares" style="left:347px;top:1108px"><span></span><span></span><span></span></div>
  <div class="abs footer-brand"><span class="dot"></span><span>PINECREST 71 STUDIOS</span></div>
</footer>
</body>
</html>
```